Business card for a boutique travel agency VELIRANDE

we need a business card design - double sided. We would like to have a very elegant, sophisticated but modern design. we are travel consultants and our business focus is Europe, mainly the city of Paris. We would like to receive designs in white and silver, black color but if you are confident that we should pick up a color to make it different and more beautful...go ahead! We are going to give business cards to our clients and business partners. It is important to be perceived as elegant, modern and trustful. Please check jpg references.

Target Market(s)

Velirande primary clients are individuals, couples and affinity groups of high-net-worth who travel for leisure at least once per year. Seeking the ultimate travel experience, the target clients demand the finest quality activities and accommodations accompanied by a superior level of service.

Industry/Entity Type

Travel Industry

Contact Information for Business Card

Liliana Quesada
- liliana@velirande-mail.example
- +55 11 98437.5216
- velirande-mail.example
- unique travel experiences (we would like to see this signature printed as a detail)

Font styles to use
Sans Serif

Colors

Designer to choose colors to be used in the design.

Requirements
Must have
• the Velirande logo that I have attached
Nice to have
• we would like to have some nice detail, something different that shows that we care about,... we are detail oriented.
Should not have
• decorative fonts

```html
<!DOCTYPE html>
<html lang="en">
<head>
<meta charset="utf-8">
<title>Velirande – Business Card</title>
<link rel="stylesheet" href="https://fonts.googleapis.com/css2?family=Josefin+Sans:wght@300&family=Open+Sans:wght@400&display=swap">
<style>
  :root {
    --backdrop: #8d8d8d;
    --card: #e9e9eb;
    --ink: #141414;
    --card-shadow: rgba(0, 0, 0, 0.28);
  }
  * { margin: 0; padding: 0; box-sizing: border-box; }
  html, body {
    width: 1200px;
    height: 782px;
    overflow: hidden;
    background: var(--backdrop);
  }
  .canvas {
    position: relative;
    width: 1200px;
    height: 782px;
  }
  .card {
    position: absolute;
    left: 358px;
    width: 452px;
    height: 250px;
    background: var(--card);
    box-shadow: 0 6px 10px var(--card-shadow);
    color: var(--ink);
  }
  .card--front { top: 104px; }
  .card--back { top: 409px; }

  .wordmark {
    position: absolute;
    left: 0;
    right: 0;
    top: 114px;
    text-align: center;
    font-family: "Josefin Sans", sans-serif;
    font-weight: 300;
    font-size: 18px;
    letter-spacing: 0.36em;
    padding-left: 0.36em;
    line-height: 22px;
  }

  .holder-name {
    position: absolute;
    left: 68px;
    top: 118px;
    font-family: "Open Sans", sans-serif;
    font-weight: 400;
    font-size: 18px;
    line-height: 22px;
  }
  .brand-dot {
    position: absolute;
    left: 211px;
    top: 117px;
    width: 24px;
    height: 24px;
  }
  .contact-list {
    position: absolute;
    left: 248px;
    top: 107px;
    list-style: none;
    font-family: "Open Sans", sans-serif;
    font-size: 10.5px;
    line-height: 14.5px;
  }
  .contact-item {
    display: flex;
    align-items: center;
  }
  .contact-icon {
    width: 8px;
    height: 8px;
    margin-right: 6px;
    flex: none;
  }
  .tagline {
    position: absolute;
    left: 0;
    right: 0;
    top: 219px;
    text-align: center;
    font-family: "Open Sans", sans-serif;
    font-size: 10.5px;
    line-height: 14px;
  }
</style>
</head>
<body>
<main class="canvas">
  <section class="card card--front" aria-label="Card front">
    <h1 class="wordmark">VELIRANDE</h1>
  </section>

  <section class="card card--back" aria-label="Card back">
    <p class="holder-name">Liliana Quesada</p>
    <svg class="brand-dot" viewBox="0 0 24 24" aria-hidden="true">
      <circle cx="12" cy="12" r="9" fill="none" stroke="currentColor" stroke-width="2"/>
    </svg>
    <ul class="contact-list">
      <li class="contact-item">
        <svg class="contact-icon" viewBox="0 0 10 10" aria-hidden="true">
          <path d="M2.2 0.8 L3.6 2.6 L2.8 3.6 Q3.8 5.8 6.2 7.1 L7.2 6.3 L9.1 7.6 L8.2 9.2 Q3.6 9 0.9 2.1 Z" fill="currentColor"/>
        </svg>
        <span>+55 11 98437.5216</span>
      </li>
      <li class="contact-item">
        <svg class="contact-icon" viewBox="0 0 10 10" aria-hidden="true">
          <rect x="0.5" y="2" width="9" height="6.5" rx="0.6" fill="currentColor"/>
          <path d="M0.9 2.5 L5 5.6 L9.1 2.5" fill="none" stroke="#e9e9eb" stroke-width="0.9"/>
        </svg>
        <span>liliana@velirande-mail.example</span>
      </li>
      <li class="contact-item">
        <svg class="contact-icon" viewBox="0 0 10 10" aria-hidden="true">
          <circle cx="5" cy="5" r="4.3" fill="currentColor"/>
          <path d="M0.8 5 H9.2 M5 0.7 V9.3 M5 0.8 Q2.4 5 5 9.2 M5 0.8 Q7.6 5 5 9.2" fill="none" stroke="#e9e9eb" stroke-width="0.7"/>
        </svg>
        <span>velirande-mail.example</span>
      </li>
    </ul>
    <p class="tagline">unique travel experiences</p>
  </section>
</main>
</body>
</html>
```